Crest Porter Website Professional and Crisp Redesign

Hi Teams,
Good evening! I am looking for a Warm Crisp and Professional redesign of my company's website at www.CrestPorter.example. Please google "Valet Trash" also to see the low rent stuff my competition is doing. I have included so much material for you to help your creative minds collaborate with. We use Wordpress now and have a mobile app plug in that is using xmlrpc to communicate back and forth iOS and Android. Swift for iOS and Java for android. Wordpress for the site. Good Luck!
Heres a little test site we fooled around with http://crest.kmorr.example to get ideas flowing, if needed.
Use the new content and redesign file for page content/copy. We all add information like Bio's when we get there.
I want you to be creative - use your own words, just be crisp about it.
Home Page:
Concept:
Nice marsh/tide/palm tree image of a community, poised up to the sky.
Crest porter sign for each of the respective redirections/pages. (4 total)
Statement:
Crest Porter is a leading valet trash and recycling service provider offering robust and flexible solutions for your community’s recycling, waste and maintenance needs. Connect with us and let us give you and your residents the experience they deserve: Better people, better processes, and better technologies.
Video –
Client Login – top left always
Slogan – Improve the day with valet.
Tabs: (Could be in boxes or the Crest Porter sign)
1. Residents
2. Property Management
3. About us
4. Contact
Residents Page:
Dear Resident,
Making sure that our environment and communities stay beautiful is a part of Crest Porter’s mission. We owe it to ourselves to be more thoughtful in our own waste production by ensuring the items we discard have fulfilled their highest and best uses. We are thankful for the steps we take together that propel us in the right direction.
Video.
Why Valet:
Crest Porter solves the embarrassment and effort of handling waste and recycling for the sophisticated multifamily resident. We always like to say – find us one person who likes to take out the trash…
Service guidelines on display and downloadable.
Oops!
Picture of an example oops note –
Get one of these?! No sweat, just correct the checked box the next night and we will happily take your trash/recycling the next scheduled service evening.
Essentials:
1. Trash is tied, bagged, and in the provided container.
(max 2 bags, 25 lbs/night)
2. Ensure bins are placed and returned at the agreed upon times.
3. Always feel free to contact us with any questions, comments, or concerns.
Management Page
Dear Management,
As our multifamily industry grows and continues to evolve with our residents, add value industries like Valet Trash are emerging as best bets for better serving your community as a whole. Knowing the industry as we do, Crest Porter knows that how we perform in New York, directly impacts our teams opportunities in Florida. By instilling this united culture we are consistently able to outperform our industry’s key performance indicators such as retention rate that affords Crest Porter the advantage in most cases.
Video:
Why Crest?
1. Our Values –
Integrity | We are transparent and forthright in what we do.
Outstanding Customer Service | For us this means doing more than just what we are compensated for.
Accountability | In our industry, it’s the one miss that is remembered, so we always have redundancy plans and the technology needed to keep our clients well rested.
Strong Work Ethic | Discipline is the cornerstone of great results, and reliability.
2. Our People –
Crest Porter hosts tryouts, not interviews for all its thoroughly background checked employees. Tryouts ensure our high standards of integrity, accountability, and strong work ethics are consistently observed before allowing them on-site alone.
3. Our Process –
Our employee’s are trained to be safe problem solvers from the start. We take a 500-foot view above the job scope to develop safer, more efficient, and through ways of improving our work and culture. Then, we listen.
4. Our Technology –
Technology has allowed Crest Porter to better bridge the communication gap for our clients to get on-site performance data real time. Our application, H2H (Hall to hall), allows fast accurate reporting of our job assignments. This tool takes out the guesswork and follow up time when we have inquires.
5. Our Dividends –
No need to budget when our service generates profit infinitely with no start up investment through our phase in programs. We will always consider buying out the current provider’s contract as requested.
6. Our Involvements –
A chief aim for Crest Porter is to uplift and connect with our teammates, our clients, and our communities. We always find brilliant ways to contribute both with micro and macro impacts consistently. Check the attendance records of your local and national meetings and events – you’ll see that we show up. We are committed.
Connect with us to inquire more information and pricing
Info@CrestPorter.example | 885- CRST-PQL
Download information package
About
Hi There,
After spilling leaking trash in a brand new car on the way to the community compactor, enough was enough. The company was formed that same evening and the founder turned in his safe executive roll for a fortune 500 company and dove into the world of the unknown – Entrepreneurship. Through the merits of our service, self-investment, and teach-ability index Crest Porter is fast becoming a stable leader in setting the standard for valet trash.
Video
Leadership
Executive Team
Ray Fenwick
Glen Matusiak
Tara Hollins
Marla Quenvick
Ingrid Falkner
Area Management
New York
South Carolina
North Carolina
Georgia
Florida
Louisiana
Alabama
Texas
Contact page:
Pretty straight forward.
Again Good Luck!
Ray Fenwick
President
Crest Porter
Target Market(s)
Professionals
Industry/Entity Type
Apartment
Number of Pages Required
5+ page
Font styles to use
Requirements
Must have
- Professional, Organized, and Crisp
Nice to have
- You go out on your own and put your own touch on it. That would be refreshing.
Should not have
- Don't use the word "Complex" to talk about apartments. Have fun!

```html
<!DOCTYPE html>
<html lang="en">
<head>
<meta charset="utf-8">
<title>Crest Porter – About Us</title>
<link href="https://fonts.googleapis.com/css2?family=Mulish:wght@400;600;700;800&family=Open+Sans:wght@400;600&display=swap" rel="stylesheet">
<style>
:root{
  --navy:#1b2f6b;
  --navy-deep:#13245a;
  --blue:#4a90d0;
  --blue-soft:#5e9ddb;
  --sky:#8fb3da;
  --footer:#81a9d4;
  --footer-bar:#b5cbe6;
  --gray:#f0f0f0;
  --ink:#222;
  --muted:#8a8a8a;
  --white:#fff;
}
*{box-sizing:border-box;margin:0;padding:0}
html,body{width:1200px;height:3220px;overflow:hidden}
body{font-family:"Mulish",sans-serif;color:var(--ink);background:var(--white);position:relative}
.abs{position:absolute}

/* top bar */
.topbar{left:0;top:0;width:1200px;height:39px;background:#f4f4f4}
.client-login{left:118px;top:0;width:127px;height:39px;background:var(--sky);color:#fff;font-size:14px;font-weight:600;display:flex;align-items:center;justify-content:center}
.social{right:127px;top:6px;display:flex;gap:6px}
.social span{width:26px;height:26px;border:2px solid var(--navy);border-radius:50%;display:block}

/* header */
.header{left:0;top:39px;width:1200px;height:116px;background:#fff;border-bottom:1px solid #e3e3e3}
.brand{left:118px;top:58px;display:flex;align-items:center;gap:10px}
.brand-mark{width:70px;height:70px;border-radius:50%;border:5px solid var(--blue)}
.brand-name{font-size:34px;font-weight:800;color:var(--navy);line-height:1}
.brand-tag{font-size:9px;color:var(--navy);margin-top:3px}
.brand-phone{font-size:15px;color:var(--navy);margin-top:2px;text-align:center}
.nav{top:39px;height:116px;display:flex;align-items:center;font-size:17px;color:#8b8b8b}
.nav a{position:absolute;text-decoration:none;color:inherit;white-space:nowrap}
.nav a.active{color:var(--navy)}
.nav-underline{left:868px;top:151px;width:100px;height:4px;background:var(--navy)}

/* hero */
.hero{left:0;top:155px;width:1200px;height:539px;background:linear-gradient(180deg,#9aa4ad 0%,#b3b7b6 38%,#7b7f6d 62%,#a99767 82%,#8c7b52 100%)}
.hero-text{left:125px;top:278px;width:880px;color:#fff}
.hero-text h1{font-size:30px;font-weight:600;margin-bottom:8px}
.hero-text p{font-size:20.5px;line-height:29px;font-weight:600}

/* titles */
.section-title{width:1200px;left:0;text-align:center;font-size:28px;font-weight:600}
.title-rule{width:62px;height:2px;left:569px}

/* video */
.video-frame{left:324px;top:809px;width:548px;height:342px;border:1px solid #d5d5d5;padding:10px;background:#fff;box-shadow:0 1px 4px rgba(0,0,0,.15)}
.video-still{width:100%;height:100%;background:linear-gradient(135deg,#d9d3c6 0%,#c9b49d 40%,#b64747 60%,#d7dde3 100%)}
.play{left:550px;top:938px}

/* executive team */
.exec{left:0;top:1198px;width:1200px;height:477px;background:linear-gradient(180deg,#2a4a8c 0%,#1c3576 45%,#14296a 100%)}
.exec-card{top:1338px;width:221px;height:236px}
.exec-photo{width:221px;height:191px;background:linear-gradient(180deg,#c9c6c2,#8d8781)}
.exec-name{height:45px;background:var(--blue-soft);color:#fff;font-size:16px;font-weight:700;display:flex;align-items:center;justify-content:center;text-transform:uppercase}
.exec-card.featured{border:3px solid #8ab6e8}
.exec-card.featured .exec-photo{height:230px;background:linear-gradient(180deg,#5d93d6,#3f7cc7)}
.featured-label{left:0;top:62px;width:215px;text-align:center;color:#fff}
.featured-label b{display:block;font-size:19px;margin-top:6px;text-transform:uppercase}

/* values */
.values{left:0;top:1675px;width:1200px;height:440px;background:var(--gray)}
.value{top:1814px;width:224px;height:224px;border-radius:50%;border:5px solid #fff;box-shadow:0 0 0 2px var(--navy);color:#fff;text-align:center;padding:52px 34px 0;font-family:"Open Sans",sans-serif}
.value.dark{background:var(--navy-deep)}
.value.light{background:var(--blue-soft);box-shadow:0 0 0 2px var(--blue-soft)}
.value h3{font-size:17px;font-weight:600;line-height:22px;margin-bottom:10px;text-transform:uppercase}
.value p{font-size:13px;line-height:20px}

/* statement */
.statement{left:0;top:2115px;width:1200px;height:730px;background:linear-gradient(180deg,#dbeaf6 0%,#edf4fa 30%,#ffffff 60%,#ffffff 100%)}
.statement-copy{left:225px;top:2220px;width:750px;text-align:center;font-family:"Open Sans",sans-serif;font-size:13.5px;line-height:23px;color:var(--muted)}
.info-card{top:2338px;width:305px;height:425px;background:#fff;border:1px solid #d8d8d8;box-shadow:0 1px 4px rgba(0,0,0,.12);padding:13px;text-align:center}
.info-img{height:210px}
.info-card h3{font-size:22px;font-weight:700;color:var(--navy-deep);margin:16px 0 8px;text-transform:uppercase}
.info-card p{font-family:"Open Sans",sans-serif;font-size:11.5px;line-height:20px;color:var(--muted);padding:0 20px}
.read-more{display:inline-block;margin-top:20px;width:122px;height:34px;line-height:34px;background:var(--blue-soft);color:#fff;font-size:13px;font-weight:600}

/* footer */
.footer{left:0;top:2845px;width:1200px;height:311px;background:var(--footer);color:#fff}
.footer-brand{left:150px;top:2900px;width:200px;text-align:center}
.footer-mark{width:90px;height:90px;border:5px solid #fff;border-radius:50%;margin:0 auto 6px}
.footer-brand .name{font-size:33px;font-weight:800;line-height:1}
.footer-brand .tag{font-size:9px;margin-top:3px}
.footer-brand .phone{font-size:17px;margin-top:4px}
.footer-col{top:2912px}
.footer-col h4{font-size:17px;font-weight:600;margin-bottom:16px;text-transform:uppercase}
.footer-col li{list-style:none;font-family:"Open Sans",sans-serif;font-size:13px;line-height:30px}
.contact-line{display:flex;align-items:flex-start;gap:10px;font-family:"Open Sans",sans-serif;font-size:13px;line-height:26px}
.copyright{left:0;top:3156px;width:1200px;height:64px;background:var(--footer-bar);color:#6a7f99;font-size:13px;display:flex;align-items:center;justify-content:center}
</style>
</head>
<body>

<div class="abs topbar"></div>
<div class="abs client-login">Client Login</div>
<div class="abs social"><span></span><span></span><span></span><span></span></div>

<header class="abs header"></header>
<div class="abs brand">
  <div class="brand-mark"></div>
  <div>
    <div class="brand-name">Crest Porter</div>
    <div class="brand-tag">Valet Waste Management Services</div>
    <div class="brand-phone">1-855-Crest PQL</div>
  </div>
</div>
<nav class="abs nav">
  <a style="left:445px">Home</a>
  <a style="left:532px">Residents</a>
  <a style="left:648px">Property Management</a>
  <a class="active" style="left:872px">About Us</a>
  <a style="left:985px">Contact</a>
</nav>
<div class="abs nav-underline"></div>

<section class="abs hero" role="img" aria-label="Marsh-side waterfront homes under a soft sky with tall grasses in front"></section>
<div class="abs hero-text">
  <h1>Hi There,</h1>
  <p>After spilling leaking trash in a brand new car on the way to the community compactor, enough was enough. The company was formed that same evening and the founder turned in his safe executive roll for a fortune 500 company and dove into the world of the unknown – Entrepreneurship. Through the merits of our service, self-investment, and teach-ability index Crest Porter is fast becoming a stable leader in setting the standard for valet trash.</p>
</div>

<h2 class="abs section-title" style="top:743px">About Video</h2>
<div class="abs title-rule" style="top:786px;background:var(--blue)"></div>
<div class="abs video-frame"><div class="video-still" role="img" aria-label="Video still of a presenter speaking in a bright office"></div></div>
<svg class="abs play" width="96" height="96" viewBox="0 0 96 96"><circle cx="48" cy="48" r="46" fill="#111"/><path d="M38 28 L68 48 L38 68 Z" fill="#fff"/></svg>

<section class="abs exec" role="img" aria-label="Dusky blue marsh and tree line behind the executive team"></section>
<h2 class="abs section-title" style="top:1255px;color:#fff;font-size:26px">Executive Team</h2>
<div class="abs title-rule" style="top:1303px;background:#8ab6e8"></div>

<div class="abs exec-card featured" style="left:118px">
  <div class="exec-photo" role="img" aria-label="Portrait of Ray Fenwick"></div>
  <div class="abs featured-label">
    <svg width="44" height="44" viewBox="0 0 44 44"><circle cx="18" cy="18" r="12" fill="none" stroke="#fff" stroke-width="4"/><line x1="27" y1="27" x2="40" y2="40" stroke="#fff" stroke-width="5" stroke-linecap="round"/></svg>
    <b>Ray Fenwick</b>
  </div>
</div>
<div class="abs exec-card" style="left:365px">
  <div class="exec-photo" role="img" aria-label="Portrait of Glen Matusiak"></div>
  <div class="exec-name">Glen Matusiak</div>
</div>
<div class="abs exec-card" style="left:612px">
  <div class="exec-photo" style="background:linear-gradient(180deg,#d8d8d8,#9a9a9a)" role="img" aria-label="Portrait of Tara Hollins"></div>
  <div class="exec-name">Tara Hollins</div>
</div>
<div class="abs exec-card" style="left:859px">
  <div class="exec-photo" style="background:linear-gradient(180deg,#cdbfae,#8f7b69)" role="img" aria-label="Portrait of Marla Quenvick"></div>
  <div class="exec-name">Marla Quenvick</div>
</div>

<section class="abs values"></section>
<h2 class="abs section-title" style="top:1736px;color:var(--blue);font-size:27px">Company History and Values</h2>
<div class="abs title-rule" style="top:1782px;background:var(--blue)"></div>
<div class="abs value dark" style="left:188px"><h3>Integrity</h3><p>We are transparent and forthright in what we do</p></div>
<div class="abs value light" style="left:378px"><h3>Outstanding Customer</h3><p>This means doing more than what we are compensated for</p></div>
<div class="abs value dark" style="left:583px"><h3>Accountability</h3><p>It's the one miss that's remembered. We have the technology needed</p></div>
<div class="abs value light" style="left:775px"><h3>Strong Work Ethic</h3><p>Discipline is the corner stone of great results, and reliability</p></div>

<section class="abs statement" role="img" aria-label="Pale misty marsh landscape fading into white"></section>
<h2 class="abs section-title" style="top:2170px;color:var(--blue);font-size:27px">Our Statement</h2>
<p class="abs statement-copy">Maecenas aliquet velit vel turpis Mauris neque metus malesuada nec ultricies sit amet porttitor mattis enim In massa libero interdum nec interdum vel blandit sed nulla In ullamcorper est eget tempor cursus neque mi consectetuer mi a ultricies massa est sed nisl Class aptent taciti sociosqu ad litora torquent</p>

<div class="abs info-card" style="left:118px">
  <div class="info-img" style="background:linear-gradient(180deg,#c7d6e6 0%,#b9b3a4 55%,#6fb3cf 100%)" role="img" aria-label="Apartment community with a pool"></div>
  <h3>Who</h3>
  <p>sociosqu ad litora torquent per conubia nostra per inceptos hymenaeos Proin nulla arcu nonummy luctus dictum eget fermentum et lorem Nunc porta convallis pede</p>
  <span class="read-more">Read More</span>
</div>
<div class="abs info-card" style="left:440px">
  <div class="info-img" style="background:linear-gradient(180deg,#b9cde0 0%,#c9a98a 50%,#6e7a4a 100%)" role="img" aria-label="Apartment buildings with a service worker in front"></div>
  <h3>Experience</h3>
  <p>sociosqu ad litora torquent per conubia nostra per inceptos hymenaeos Proin nulla arcu nonummy luctus dictum eget fermentum et lorem Nunc porta convallis pede</p>
  <span class="read-more">Read More</span>
</div>
<div class="abs info-card" style="left:762px">
  <div class="info-img" style="background:linear-gradient(180deg,#e4e6e8,#d3d8dc)" role="img" aria-label="Map of the United States showing service locations"></div>
  <h3>Location</h3>
  <p>sociosqu ad litora torquent per conubia nostra per inceptos hymenaeos Proin nulla arcu nonummy luctus dictum eget fermentum et lorem Nunc porta convallis pede</p>
  <span class="read-more">Read More</span>
</div>

<footer class="abs footer"></footer>
<div class="abs footer-brand">
  <div class="footer-mark"></div>
  <div class="name">Crest Porter</div>
  <div class="tag">Valet Waste Management Services</div>
  <div class="phone">1-855-Crest PQL</div>
</div>
<div class="abs footer-col" style="left:428px;color:#fff">
  <h4>Quick Links</h4>
  <ul><li>Residents</li><li>Property Management</li><li>About us</li><li>Contact</li></ul>
</div>
<div class="abs footer-col" style="left:662px;color:#fff">
  <h4>Resources</h4>
  <ul><li>Client Login</li><li>Blogs</li><li>Contact Us</li></ul>
</div>
<div class="abs footer-col" style="left:883px;color:#fff">
  <h4>Contact Info</h4>
  <div class="contact-line" style="font-weight:600;margin-top:-8px">Crest Porter</div>
  <div class="contact-line">
    <svg width="14" height="20" viewBox="0 0 14 20" style="margin-top:4px"><path d="M7 0C3 0 0 3 0 7c0 5 7 13 7 13s7-8 7-13c0-4-3-7-7-7z" fill="#fff"/><circle cx="7" cy="7" r="2.5" fill="#81a9d4"/></svg>
    <span>4180 Harbor Mill Rd. Ste.<br>3B Beaufort SC 29906</span>
  </div>
  <div class="contact-line" style="margin-top:6px">
    <svg width="16" height="16" viewBox="0 0 16 16" style="margin-top:5px"><path d="M3 1l3 3-2 2c1 2 3 4 5 5l2-2 3 3-2 3C6 15 1 10 1 3z" fill="none" stroke="#fff" stroke-width="1.4"/></svg>
    <span>1.855.Crest.PQL</span>
  </div>
  <div class="contact-line" style="margin-top:4px">
    <svg width="16" height="12" viewBox="0 0 16 12" style="margin-top:7px"><rect x="0.7" y="0.7" width="14.6" height="10.6" fill="none" stroke="#fff" stroke-width="1.4"/><path d="M1 1l7 6 7-6" fill="none" stroke="#fff" stroke-width="1.4"/></svg>
    <span>Info@CrestPorter.example</span>
  </div>
</div>
<div class="abs copyright">© 2017 Company Name &nbsp;All right reserved</div>

</body>
</html>
```